Brenwo Tiling Solutions Needs A Web Design

We have been a sole trader but now started a new company. We need a web page designed around our new company. We are wall and floor tilers with over 20 years experience.
A Gold Coast family owned business, with over 20 years of experience, Dalton Krusey is proud to be a trusted name for all aspects of Wall and Floor Tiling Services servicing the Gold Coast to Brisbane, Tweed Heads to Mt Tamborine.

With an eye for detail we strive for perfection with the resources to work closely with designers, architects, contractors, and home owners, delivering the best possible service in wall and floor tiling.

We will be more than glad to provide our expertise and can consult or advice you to help you make the decisions that are right for you.

Renovations should always be seen as an investment not an expense. With an ultimate goal of utmost satisfaction, our trained and qualified tradesmen will provide you exceptional services. We are well equipped with latest tools and techniques to ensure that everything is done correctly with attention paid to the smallest details.
Updates

Hello I may not have been very clear. My husband Dalton Krusey is a tiler and we used just a basic PDF flyer "Company profile" when sending our quotations. He now has decided to use a company name and so I would like a web design page for this company "Brenwo Tiling Solutions Pty Ltd" I would like to use the information as stated (in the company profile PDF) BUT under the name Brenwo - I will look into a more detailed look into the description of the job and repost the details - unfortunately I will not be able to do sometime in the next 2 days. I will then repost. My apologies for this Thank You Mae-Lin Krusey

Target Market(s)

Our clients we are aiming at are Builders domestic(homes) and commercial (shops, duplexs & 3 storey units, resort pools) plus home owners looking to renovate existing tiled areas or lay new tiles to new homes. Internal pool and pool surround

Number of Pages Required

3 page

Font styles to use
Serif

Colors
9bcb3b
ec1f27
fbed22

Requirements
Must have
• We like fluro green and black colours. and use the name Dalton Krusey (the owner) as he does the tiling labour and is the one with the expertise.
• The final design should communicate professional workmanship. quality and expertise in ALL aspects of tiling,We have pride in our workmanship and do not cut corners so that the job is done right the first time to the correct standards. Our good name is our reputation.
• I have attached a logo which we would like in fluro green and black. The person in the logo has a hammer - we want to get rid of the hammer as that is for carpentry and we are floor tilers. If another tool ie mallet can be replaced. Can you do that?
Nice to have
• Photos - highlights stand out - nice borders. classic design.

```html
<!DOCTYPE html>
<html lang="en">
<head>
<meta charset="utf-8">
<title>Brenwo Tiling Solutions</title>
<link rel="stylesheet" href="https://fonts.googleapis.com/css2?family=Roboto:ital,wght@0,300;0,400;0,500;0,700;1,300&family=Roboto+Condensed:wght@700&display=swap">
<style>
:root{
  --green:#8dc63f;
  --green-dark:#7cb32e;
  --red:#e8232a;
  --yellow:#fbed22;
  --ink:#333;
  --muted:#666;
  --band:#efefef;
  --white:#fff;
}
*{margin:0;padding:0;box-sizing:border-box}
html,body{width:774px;height:1200px;overflow:hidden}
body{position:relative;background:var(--white);font-family:"Roboto",sans-serif;color:var(--ink)}
.abs{position:absolute}
.header{left:0;top:0;width:774px;height:80px;background:linear-gradient(#fbed22 0%,#fdf7a8 35%,#fff 100%)}
.brand-mark{left:49px;top:26px;width:40px;height:40px;background:var(--green)}
.brand-name{left:100px;top:29px;font-size:14.5px;font-weight:700;color:#3a3a3a;letter-spacing:.3px}
.brand-tag{left:100px;top:51px;font-size:7.5px;color:#444;letter-spacing:.2px}
.call{right:48px;top:35px;font-size:10.5px;font-weight:500;color:var(--red);display:flex;align-items:center;gap:7px}
.nav{left:49px;top:82px;width:677px;height:33px;background:var(--green);display:flex;align-items:center;font-size:8.5px;font-weight:500;color:#fff;box-shadow:0 4px 12px rgba(0,0,0,.15)}
.nav span{flex:1;text-align:center}
.nav .active{flex:0 0 76px;background:var(--red);height:33px;line-height:33px}
.hero{left:49px;top:115px;width:677px;height:248px;background:linear-gradient(160deg,#5a6a5e 0%,#9aa3a7 40%,#3f4b4a 70%,#2d3b30 100%);box-shadow:0 14px 18px -10px rgba(0,0,0,.35)}
.hero-title{left:49px;top:208px;width:677px;text-align:center;font-family:"Roboto Condensed",sans-serif;font-weight:700;font-size:29px;color:#fff;text-shadow:0 1px 3px rgba(0,0,0,.5)}
.hero-sub{left:49px;top:246px;width:677px;text-align:center;font-size:14.5px;color:#fff;text-shadow:0 1px 3px rgba(0,0,0,.5)}
.dots{left:361px;top:323px;display:flex;gap:6px}
.dots i{width:8px;height:8px;border-radius:50%;background:#fff}
.dots i:first-child{background:var(--yellow)}
.welcome h2{font-size:13.5px;font-weight:500;color:#333;margin-bottom:12px}
.welcome{left:49px;top:399px;width:446px}
.welcome p{font-size:8.4px;font-weight:300;line-height:16px;color:#555;margin-bottom:4px}
.btn{display:inline-block;margin-top:12px;width:83px;height:29px;line-height:29px;text-align:center;background:var(--green);color:#fff;font-size:8.5px;box-shadow:0 1px 3px rgba(0,0,0,.25)}
.reviews{left:512px;top:401px;width:214px;height:150px;background:var(--green);color:#fff;padding:16px 13px}
.reviews h3{font-size:13px;font-weight:500;color:#222;display:flex;justify-content:space-between}
.reviews p{margin-top:12px;font-size:8.2px;font-style:italic;font-weight:300;line-height:16px}
.reviews .who{margin-top:11px;font-size:8.2px;color:var(--red);font-weight:500}
.services{left:0;top:569px;width:774px;height:235px;background:var(--band)}
.sec-title{width:774px;text-align:center;font-size:13px;color:#333;font-weight:500;letter-spacing:.3px}
.card{width:220px;height:141px;background:#fff;padding:3px;border:1px solid #ddd}
.card div{width:100%;height:100%}
.caption{font-size:9.8px;font-weight:500;color:#333}
.why-icon{width:61px;height:61px;border:1.5px solid var(--red);border-radius:50%;display:flex;align-items:center;justify-content:center}
.why-label{width:240px;text-align:center;font-size:10.5px;color:#333;letter-spacing:.2px}
.footer{left:0;top:1086px;width:774px;height:114px;background:var(--green)}
.foot-nav{left:49px;top:1117px;display:flex;gap:17px;font-size:7px;font-weight:500;color:#fff}
.copy{left:49px;top:1143px;font-size:6.8px;color:#fff}
.abn{left:49px;top:1160px;font-size:6.8px;color:var(--red);font-weight:500}
.follow{left:590px;top:1117px;font-size:7px;font-weight:500;color:#222}
.social{left:590px;top:1137px;display:flex;gap:3.5px}
.social i{width:20px;height:20px;border-radius:50%;background:#3d4a2a}
</style>
</head>
<body>
<div class="abs header"></div>
<div class="abs brand-mark"></div>
<div class="abs brand-name">BRENWO TILING SOLUTIONS PTY LTD</div>
<div class="abs brand-tag">WALL AND FLOOR TILING SPECIALIST</div>
<div class="abs call">
  <svg width="12" height="12" viewBox="0 0 12 12"><rect width="12" height="12" rx="2" fill="#e8232a"/><path d="M3.2 2.6l1.4-.3.8 1.8-.9.7c.4.9 1.1 1.6 2 2l.7-.9 1.8.8-.3 1.4c-3 .3-5.8-2.5-5.5-5.5z" fill="#fff"/></svg>
  CALL DALTON KRUSEY ON 0400 918 274
</div>

<nav class="abs nav">
  <span class="active">HOME</span><span>ABOUT US</span><span>OUR SERVICES</span><span>WHY CHOOSE US?</span><span>PHOTO GALLERY</span><span>REVIEWS</span><span>CONTACT US</span>
</nav>

<div class="abs hero" role="img" aria-label="Tiler at work on a large tiled waterfront terrace with steps and pool"></div>
<div class="abs hero-title">WALL AND FLOOR TILING SPECIALIST</div>
<div class="abs hero-sub">A Gold Coast family owned business, with over 20 years of experience.</div>
<div class="abs dots"><i></i><i></i><i></i><i></i></div>

<section class="abs welcome">
  <h2>WELCOME TO&nbsp; BRENWO TILING SOLUTIONS</h2>
  <p>A Gold Coast family owned business, with over 20 years of experience, Dalton Krusey Tiling is proud to be a trusted name for all aspects of Wall and Floor Tiling Services servicing the Gold Coast to Brisbane, Tweed Heads to Mt Tamborine.</p>
  <p>With an eye for detail we strive for perfection with the resources to work closely with designers, architects, contractors, and home owners, delivering the best possible service in wall and floor tiling.</p>
  <span class="btn">READ MORE</span>
</section>

<aside class="abs reviews">
  <h3>REVIEWS
    <svg width="28" height="12" viewBox="0 0 28 12"><path d="M7 1L2 6l5 5M20 1l5 5-5 5" stroke="#fff" stroke-width="2" fill="none"/></svg>
  </h3>
  <p>We purchased a house just before xmas and thought our chances of getting a tiler straight after xmas may have been difficult.We contacted Dalton who arrived on time...</p>
  <div class="who">- Grant &amp; Leanne</div>
</aside>

<section class="abs services"></section>
<div class="abs sec-title" style="left:0;top:583px">OUR SERVICES</div>
<svg class="abs" style="left:25px;top:693px" width="10" height="16" viewBox="0 0 10 16"><path d="M8 1L2 8l6 7" stroke="#ccc" stroke-width="1.5" fill="none"/></svg>
<div class="abs card" style="left:49px;top:613px"><div role="img" aria-label="Polished marble floor with dark tiled staircase" style="background:linear-gradient(135deg,#d9d6d0,#b9aa95 60%,#3a3a3a)"></div></div>
<div class="abs card" style="left:277px;top:613px"><div role="img" aria-label="Blue tiled swimming pool with coping" style="background:linear-gradient(#4a7f3a 0%,#1e9be0 15%,#2fb5f0 100%)"></div></div>
<div class="abs card" style="left:505px;top:613px"><div role="img" aria-label="Commercial outdoor tiled terrace with fire pit" style="background:linear-gradient(135deg,#6a6e6c,#e6e8ea 45%,#2a2a2a)"></div></div>
<div class="abs caption" style="left:50px;top:771px">WALL AND FLOOR TILING</div>
<div class="abs caption" style="left:278px;top:771px">SWIMMING POOLS, COPING &amp; POOL</div>
<div class="abs caption" style="left:506px;top:771px">COMMERCIAL AND RESIDENTIAL TILING</div>

<div class="abs sec-title" style="left:0;top:828px">WHY CHOOSE US ?</div>

<div class="abs why-icon" style="left:124px;top:863px"><svg width="28" height="30" viewBox="0 0 28 30"><circle cx="14" cy="11" r="8" fill="#e8232a"/><circle cx="14" cy="11" r="4" fill="#fff"/><path d="M9 17l-3 11 4-2 3 3 1-10M19 17l3 11-4-2-3 3-1-10" fill="#e8232a"/></svg></div>
<div class="abs why-icon" style="left:356px;top:863px"><svg width="28" height="30" viewBox="0 0 28 30"><rect x="3" y="6" width="13" height="20" rx="1" fill="none" stroke="#e8232a" stroke-width="2"/><path d="M6 12h7M6 16h7M6 20h5" stroke="#e8232a" stroke-width="1.5"/><path d="M14 28c0-6 3-9 7-9s6 3 6 9z" fill="#e8232a"/><path d="M16 10a5 5 0 0 1 10 0z" fill="#e8232a"/></svg></div>
<div class="abs why-icon" style="left:588px;top:863px"><svg width="30" height="30" viewBox="0 0 30 30"><rect x="2" y="12" width="26" height="6" transform="rotate(45 15 15)" fill="none" stroke="#e8232a" stroke-width="1.8"/><path d="M24 4l2 2L9 23l-4 1 1-4z" fill="none" stroke="#e8232a" stroke-width="1.8"/></svg></div>
<div class="abs why-label" style="left:34px;top:936px">Satisfaction Guaranteed</div>
<div class="abs why-label" style="left:267px;top:936px">Qualified Workmanship</div>
<div class="abs why-label" style="left:498px;top:936px">Free Measure and Quote</div>

<div class="abs why-icon" style="left:124px;top:975px"><svg width="28" height="28" viewBox="0 0 28 28"><rect x="5" y="4" width="12" height="22" fill="none" stroke="#e8232a" stroke-width="2"/><rect x="17" y="12" width="7" height="14" fill="none" stroke="#e8232a" stroke-width="2"/><path d="M8 8h6M8 12h6M8 16h6M8 20h6M19 16h3M19 20h3" stroke="#e8232a" stroke-width="1.5"/></svg></div>
<div class="abs why-icon" style="left:356px;top:975px"><svg width="28" height="28" viewBox="0 0 28 28"><path d="M5 3h12l5 5v17H5z" fill="none" stroke="#e8232a" stroke-width="2"/><path d="M8 10h8M8 14h6M8 18h4" stroke="#e8232a" stroke-width="1.5"/><path d="M24 9l3 3-10 10-4 1 1-4z" fill="#e8232a"/></svg></div>
<div class="abs why-icon" style="left:588px;top:975px"><svg width="30" height="28" viewBox="0 0 30 28"><path d="M8 6c2 4 4 6 4 9a4 4 0 0 1-8 0c0-3 2-5 4-9zM22 6c2 4 4 6 4 9a4 4 0 0 1-8 0c0-3 2-5 4-9zM15 2c1.5 3 3 4.5 3 6.5a3 3 0 0 1-6 0C12 6.5 13.5 5 15 2z" fill="#e8232a"/><rect x="2" y="23" width="26" height="2.5" fill="#e8232a"/></svg></div>
<div class="abs why-label" style="left:34px;top:1047px">Residential and Commercial Services</div>
<div class="abs why-label" style="left:267px;top:1047px">QBCC Licenced for Wall and Floor Tiling</div>
<div class="abs why-label" style="left:498px;top:1047px">QBCC Licenced for Waterproofing</div>

<footer class="abs footer"></footer>
<div class="abs foot-nav"><span>HOME</span><span>ABOUT US</span><span>OUR SERVICES</span><span>WHY CHOOSE US?</span><span>PHOTO GALLERY</span><span>REVIEWS</span><span>CONTACT US</span></div>
<div class="abs copy">Copyright © 2016.&nbsp; Brenwo Tiling Solutions&nbsp; All Right Reserved</div>
<div class="abs abn">ABN&nbsp; 48 102 775 319&nbsp; - BSA Licence 70482</div>
<div class="abs follow">FOLLOW US</div>
<div class="abs social"><i></i><i></i><i></i><i></i><i></i><i></i></div>
</body>
</html>
```